Mailer Postcard for Potential Bankruptcy Clients

The postcard will be printed at 8.5"x6" to abide by the specification at the following link: https://www.mailvortex.example/art-upload/guide/. I want an attractive two sided post card that includes my logo (see attachment). The design would have to have room for the website address, phone number, two location addresses and give them information about a civil action pending against them (You are being sued in X county (case# xxyx). We can help.). I don't really like the visuals of the attached postcard, so please use as a general guide for what I am trying to do. Ultimately, I want an ad that gets people to call me so I can help them.

I also want it to be compatible with the website (CreditHarbor.Legal).

Target Market(s)

Potential bankruptcy clients.

Industry/Entity Type

Legal

Colors

Designer to choose colors to be used in the design.

Requirements
Must have
• Phone number, addresses, website, and place for text regarding pending legal action against the receiver. Should say something to the effect: You have a pending legal action in (county name) County (court name [superior, magistrate, ect.]). Let us help you deal with it responsibly.
• Please note the design specifications at this link:

```html
<!DOCTYPE html>
<html lang="en">
<head>
<meta charset="utf-8">
<title>Credit Harbor Law Group – Mailer Postcard</title>
<link rel="stylesheet" href="https://fonts.googleapis.com/css2?family=Bebas+Neue&family=Catamaran:wght@400;500;600&family=Oswald:wght@300&display=swap">
<style>
  :root {
    --green: #4cb84a;
    --green-soft: #6cc26a;
    --green-text: #3fae3d;
    --ink: #3a3a3a;
    --ink-soft: #555;
    --band: #f2f2f2;
    --grey-box: #a9a9ab;
    --page: #e6e6e6;
    --white: #ffffff;
  }
  * { box-sizing: border-box; margin: 0; padding: 0; }
  html, body { width: 841px; height: 1200px; overflow: hidden; }
  body {
    background: var(--page);
    font-family: "Catamaran", sans-serif;
    color: var(--ink);
    position: relative;
  }
  .postcard {
    position: absolute;
    left: 96px;
    width: 635px;
    height: 449px;
    background: var(--white);
    overflow: hidden;
    box-shadow: 0 2px 8px rgba(0,0,0,.18);
  }
  .postcard--front { top: 112px; }
  .postcard--back { top: 657px; }

  /* ---------- Front ---------- */
  .hero { position: absolute; left: 0; top: 0; width: 635px; height: 251px; }
  .hero__photo {
    position: absolute; inset: 0;
    background: linear-gradient(180deg, #cfd6cf 0%, #efe3bf 45%, #b8a064 70%, #7b6a3a 100%);
  }
  .hero__panel { position: absolute; inset: 0; }
  .headline {
    position: absolute; right: 66px; top: 62px;
    text-align: right;
    font-family: "Bebas Neue", sans-serif;
    font-size: 46px; line-height: 45px;
    color: var(--white);
  }
  .headline span { display: inline-block; background: var(--green); padding: 0 2px 0 6px; }

  .brand-band { position: absolute; left: 0; top: 251px; width: 635px; height: 108px; background: var(--band); }
  .brand {
    position: absolute; display: flex; align-items: center; gap: 10px;
  }
  .brand__dot { width: 46px; height: 46px; border-radius: 50%; background: var(--green-soft); flex: none; }
  .brand__name { font-weight: 500; font-size: 22px; line-height: 24px; color: var(--ink); }
  .brand--front { left: 28px; top: 31px; }

  .pending { position: absolute; left: 321px; top: 17px; width: 265px; }
  .pending__lead { font-size: 16px; color: var(--ink-soft); }
  .pending__field { margin-top: 3px; width: 262px; height: 33px; background: var(--white); }
  .pending__offer { margin-top: 5px; font-size: 14.5px; color: var(--green-text); }

  .contact-row { position: absolute; left: 0; top: 359px; width: 635px; height: 68px; }
  .appointment { position: absolute; left: 27px; top: 13px; }
  .appointment__label { font-size: 11.5px; line-height: 14px; }
  .appointment__phone { display: flex; align-items: center; gap: 6px; font-size: 21px; line-height: 26px; color: var(--ink-soft); }
  .divider { position: absolute; top: 16px; width: 1px; height: 36px; background: var(--green); }
  .address { position: absolute; top: 19px; font-size: 11px; line-height: 15px; color: var(--ink); }
  .web-bar {
    position: absolute; left: 0; top: 427px; width: 635px; height: 22px;
    background: var(--green); color: var(--white);
    font-size: 11.5px; line-height: 22px; text-align: right; padding-right: 25px;
  }

  /* ---------- Back ---------- */
  .intro {
    position: absolute; left: 0; top: 0; width: 635px; height: 97px;
    background: linear-gradient(100deg, #56bb54 0%, #66c264 60%, #7acb78 100%);
  }
  .intro__text {
    position: absolute; left: 21px; top: 12px; width: 500px;
    font-size: 21.5px; line-height: 25px; color: var(--white); font-weight: 500;
  }
  .stamp { position: absolute; left: 545px; top: 10px; width: 80px; height: 79px; background: var(--white); border: 1px solid #777; }
  .about { position: absolute; left: 0; top: 97px; width: 635px; height: 61px; background: var(--band); }
  .about p { position: absolute; left: 21px; right: 16px; top: 9px; font-size: 9.6px; line-height: 14.5px; color: var(--ink-soft); text-align: justify; }
  .services { position: absolute; left: 22px; top: 175px; list-style: none; }
  .services li { display: flex; align-items: center; gap: 8px; font-size: 13.6px; line-height: 21.8px; color: var(--ink); }
  .brand--back { left: 370px; top: 198px; }
  .address-space { position: absolute; left: 384px; top: 369px; width: 200px; text-align: center; font-family: "Oswald", sans-serif; font-weight: 300; color: #777; }
  .address-space__small { font-size: 7.5px; letter-spacing: 2px; }
  .address-space__big { font-size: 14px; letter-spacing: 7px; line-height: 16px; }
  .call-box { position: absolute; left: 0; top: 391px; width: 230px; height: 58px; background: var(--grey-box); color: var(--white); padding: 6px 0 0 22px; }
  .call-box__label { font-size: 13px; line-height: 17px; }
  .call-box__phone { display: flex; align-items: center; gap: 5px; font-size: 21px; line-height: 26px; }
</style>
</head>
<body>

<section class="postcard postcard--front">
  <div class="hero">
    <div class="hero__photo" role="img" aria-label="Photo of a man in shirt and tie with arms raised in a golden field at sunset"></div>
    <svg class="hero__panel" width="635" height="251" viewBox="0 0 635 251" aria-hidden="true">
      <polygon points="460,0 635,0 635,251 311,251" fill="#4cb84a"/>
    </svg>
    <h1 class="headline"><span>Get out of debt and</span><br><span>Restore your</span><br><span>Credit</span></h1>
  </div>

  <div class="brand-band">
    <div class="brand brand--front">
      <span class="brand__dot"></span>
      <span class="brand__name">Credit Harbor<br>Law Group</span>
    </div>
    <div class="pending">
      <p class="pending__lead">You have a pending legal action in</p>
      <div class="pending__field"></div>
      <p class="pending__offer">Let us help you deal with it responsibly.</p>
    </div>
  </div>

  <div class="contact-row">
    <div class="appointment">
      <p class="appointment__label">Schedule an appointment</p>
      <p class="appointment__phone">
        <svg width="14" height="14" viewBox="0 0 24 24" aria-hidden="true"><path d="M6.6 10.8a15.1 15.1 0 0 0 6.6 6.6l2.2-2.2a1 1 0 0 1 1-.25 11.4 11.4 0 0 0 3.6.57 1 1 0 0 1 1 1V20a1 1 0 0 1-1 1A17 17 0 0 1 3 4a1 1 0 0 1 1-1h3.5a1 1 0 0 1 1 1c0 1.25.2 2.45.57 3.57a1 1 0 0 1-.25 1z" fill="#555"/></svg>
        (404) 555-0182
      </p>
    </div>
    <span class="divider" style="left:231px"></span>
    <p class="address" style="left:244px">418 Magnolia Ave., NW Suite #1400<br>Atlanta, Georgia 30308</p>
    <span class="divider" style="left:446px"></span>
    <p class="address" style="left:464px">5125 Cedar Ridge Rd.<br>Douglasville, Georgia 30135</p>
  </div>
  <div class="web-bar">www.creditharbor.legal</div>
</section>

<section class="postcard postcard--back">
  <div class="intro" role="img" aria-label="Faint background photo of financial statements and invoices tinted green">
    <h2 class="intro__text">We are a Georgia Law Firm that is dedicated to being a one-stop shop for all debt woes that Georgians face.</h2>
  </div>
  <div class="stamp"></div>
  <div class="about">
    <p>We are experienced bankruptcy attorneys that understand that people need more than just a bankruptcy lawyer. People need someone that is experienced in handling all of the practical aspects of avoiding bankruptcy, recovering from bankruptcy quickly, tackling stubborn student loans, and punishing abusive debt collectors when they violate the law.</p>
  </div>

  <ul class="services">
    <li><svg width="10" height="10" viewBox="0 0 10 10" aria-hidden="true"><rect x=".5" y="1.5" width="8" height="8" fill="none" stroke="#4cb84a"/><path d="M2 5l2 2 5-6" fill="none" stroke="#4cb84a" stroke-width="1.3"/></svg>Free Credit Education Program</li>
    <li><svg width="10" height="10" viewBox="0 0 10 10" aria-hidden="true"><rect x=".5" y="1.5" width="8" height="8" fill="none" stroke="#4cb84a"/><path d="M2 5l2 2 5-6" fill="none" stroke="#4cb84a" stroke-width="1.3"/></svg>$0 Down Bankruptcy Options</li>
    <li><svg width="10" height="10" viewBox="0 0 10 10" aria-hidden="true"><rect x=".5" y="1.5" width="8" height="8" fill="none" stroke="#4cb84a"/><path d="M2 5l2 2 5-6" fill="none" stroke="#4cb84a" stroke-width="1.3"/></svg>Stop Collection Calls</li>
    <li><svg width="10" height="10" viewBox="0 0 10 10" aria-hidden="true"><rect x=".5" y="1.5" width="8" height="8" fill="none" stroke="#4cb84a"/><path d="M2 5l2 2 5-6" fill="none" stroke="#4cb84a" stroke-width="1.3"/></svg>Stop Foreclosures &amp; Repossessions</li>
    <li><svg width="10" height="10" viewBox="0 0 10 10" aria-hidden="true"><rect x=".5" y="1.5" width="8" height="8" fill="none" stroke="#4cb84a"/><path d="M2 5l2 2 5-6" fill="none" stroke="#4cb84a" stroke-width="1.3"/></svg>Stop Garnishments</li>
    <li><svg width="10" height="10" viewBox="0 0 10 10" aria-hidden="true"><rect x=".5" y="1.5" width="8" height="8" fill="none" stroke="#4cb84a"/><path d="M2 5l2 2 5-6" fill="none" stroke="#4cb84a" stroke-width="1.3"/></svg>Fix Credit Report Errors</li>
    <li><svg width="10" height="10" viewBox="0 0 10 10" aria-hidden="true"><rect x=".5" y="1.5" width="8" height="8" fill="none" stroke="#4cb84a"/><path d="M2 5l2 2 5-6" fill="none" stroke="#4cb84a" stroke-width="1.3"/></svg>Prosecute Illegal Debt Collection Practices</li>
    <li><svg width="10" height="10" viewBox="0 0 10 10" aria-hidden="true"><rect x=".5" y="1.5" width="8" height="8" fill="none" stroke="#4cb84a"/><path d="M2 5l2 2 5-6" fill="none" stroke="#4cb84a" stroke-width="1.3"/></svg>Prosecute Post Discharge Violations</li>
    <li><svg width="10" height="10" viewBox="0 0 10 10" aria-hidden="true"><rect x=".5" y="1.5" width="8" height="8" fill="none" stroke="#4cb84a"/><path d="M2 5l2 2 5-6" fill="none" stroke="#4cb84a" stroke-width="1.3"/></svg>Student Loan Representation</li>
  </ul>

  <div class="brand brand--back">
    <span class="brand__dot"></span>
    <span class="brand__name">Credit Harbor<br>Law Group</span>
  </div>

  <div class="address-space">
    <p class="address-space__small">THIS SPACE RESERVED FOR</p>
    <p class="address-space__big">ADDRESSING</p>
  </div>

  <div class="call-box">
    <p class="call-box__label">Schedule an appointment</p>
    <p class="call-box__phone">
      <svg width="14" height="14" viewBox="0 0 24 24" aria-hidden="true"><path d="M6.6 10.8a15.1 15.1 0 0 0 6.6 6.6l2.2-2.2a1 1 0 0 1 1-.25 11.4 11.4 0 0 0 3.6.57 1 1 0 0 1 1 1V20a1 1 0 0 1-1 1A17 17 0 0 1 3 4a1 1 0 0 1 1-1h3.5a1 1 0 0 1 1 1c0 1.25.2 2.45.57 3.57a1 1 0 0 1-.25 1z" fill="#fff"/></svg>
      (404) 555-0182
    </p>
  </div>
</section>

</body>
</html>
```